Orvel Crest Holdings Ltd
Creative Brief
Dara Kolby
COO
27B Hollin Row, London, E3 9TQ
dk@orvelcrest.co.uk
27b Hollin Row
Just the logo and the company's name on the green background

```html
<!DOCTYPE html>
<html lang="en">
<head>
<meta charset="utf-8">
<title>Orvel Crest Holdings Ltd – Email Signature &amp; Banner</title>
<link rel="stylesheet" href="https://fonts.googleapis.com/css2?family=Cormorant+Garamond:wght@400;500;600&display=swap">
<style>
  :root {
    --page: #ffffff;
    --card-light: #ffffff;
    --card-dark: #3a3e2e;
    --gold: #b8995c;
    --gold-soft: #cdb47f;
    --ink: #3f3f3f;
    --ink-soft: #5a5a5a;
    --cream: #f3ede0;
    --rule: #d8cdb4;
  }
  * { margin: 0; padding: 0; box-sizing: border-box; }
  html, body { width: 1200px; height: 684px; overflow: hidden; background: var(--page); }
  body { position: relative; font-family: "Cormorant Garamond", Georgia, serif; }

  .card { position: absolute; left: 96px; width: 1008px; }
  .card-frame { position: absolute; inset: 9px; border: 1.5px solid var(--gold); pointer-events: none; }

  .signature { top: 12px; height: 314px; background: var(--card-light); border: 1px solid var(--rule); box-shadow: 0 1px 4px rgba(0,0,0,.08); }
  .banner { top: 348px; height: 319px; background: var(--card-dark); }

  .contact-list { position: absolute; left: 44px; top: 160px; list-style: none; font-size: 17px; color: var(--ink-soft); line-height: 1.15; }
  .contact-list li { position: relative; padding-left: 28px; margin-bottom: 12px; }
  .contact-list li.address { margin-bottom: 14px; }
  .contact-icon { position: absolute; left: 0; top: 2px; width: 14px; height: 16px; }
  .contact-divider { position: absolute; left: 264px; top: 156px; width: 1px; height: 140px; background: var(--rule); }

  .brand-mark { position: absolute; left: 50%; border-radius: 50%; border: 2px solid var(--gold); }
  .brand-name { position: absolute; left: 0; right: 0; text-align: center; text-transform: uppercase; font-weight: 500; white-space: nowrap; line-height: 1; }
  .brand-name-main { letter-spacing: 0.04em; }
  .brand-name-sub { letter-spacing: 0.08em; }

  .signature .brand-mark { top: 26px; width: 112px; height: 112px; margin-left: -56px; }
  .signature .brand-name { color: var(--gold); }
  .signature .brand-name-main { top: 148px; font-size: 44px; }
  .signature .brand-name-sub { top: 196px; font-size: 13px; }

  .name-rule { position: absolute; left: 360px; width: 288px; top: 222px; height: 1px; background: var(--gold-soft); }
  .name-rule::after { content: ""; position: absolute; left: 50%; top: -3px; width: 7px; height: 7px; margin-left: -3.5px; border-radius: 50%; background: var(--gold); }

  .person { position: absolute; left: 0; right: 0; top: 238px; text-align: center; }
  .person-name { font-size: 34px; font-weight: 600; color: var(--ink); line-height: 1; }
  .person-role { margin-top: 4px; font-size: 14px; letter-spacing: 0.08em; color: var(--gold); }

  .banner .brand-mark { top: 32px; width: 126px; height: 126px; margin-left: -63px; }
  .banner .brand-name { color: var(--cream); }
  .banner .brand-name-main { top: 184px; font-size: 52px; }
  .banner .brand-name-sub { top: 244px; font-size: 16px; }
</style>
</head>
<body>

<section class="card signature" aria-label="Email signature">
  <div class="card-frame"></div>

  <ul class="contact-list">
    <li class="address">
      <svg class="contact-icon" viewBox="0 0 14 16" aria-hidden="true"><path d="M7 1a5 5 0 0 0-5 5c0 3.6 5 9 5 9s5-5.4 5-9a5 5 0 0 0-5-5z" fill="var(--gold)"/><circle cx="7" cy="6" r="1.8" fill="#fff"/></svg>
      27B Hollin Row,<br>London, E3 9TQ
    </li>
    <li>
      <svg class="contact-icon" viewBox="0 0 14 16" aria-hidden="true"><path d="M3 2l2.5-.5 1.5 3.5-1.6 1.2a8 8 0 0 0 3.4 3.4L10 8l3.5 1.5L13 12c-.4 1.3-2 2-3.5 1.5C5.8 12.3 2.7 9.2 1.5 5.5 1 4 1.7 2.4 3 2z" fill="var(--gold)"/></svg>
      +44 (0)20 7946 0321
    </li>
    <li>
      <svg class="contact-icon" viewBox="0 0 14 16" aria-hidden="true"><rect x="3" y="1" width="8" height="14" rx="1.5" fill="none" stroke="var(--gold)" stroke-width="1.6"/><circle cx="7" cy="12.3" r="0.9" fill="var(--gold)"/></svg>
      +44 (0)77 0090 0412
    </li>
    <li>
      <svg class="contact-icon" viewBox="0 0 14 16" aria-hidden="true"><rect x="1" y="4" width="12" height="9" rx="1" fill="var(--gold)"/><path d="M1.5 4.5L7 9l5.5-4.5" fill="none" stroke="#fff" stroke-width="1.2"/></svg>
      dk@orvelcrest.co.uk
    </li>
  </ul>
  <div class="contact-divider"></div>

  <span class="brand-mark" aria-hidden="true"></span>
  <span class="brand-name brand-name-main">Orvel Crest</span>
  <span class="brand-name brand-name-sub">Holdings Ltd</span>

  <div class="name-rule"></div>

  <div class="person">
    <p class="person-name">Dara Kolby</p>
    <p class="person-role">COO</p>
  </div>
</section>

<section class="card banner" aria-label="Company banner">
  <div class="card-frame"></div>
  <span class="brand-mark" aria-hidden="true"></span>
  <span class="brand-name brand-name-main">Orvel Crest</span>
  <span class="brand-name brand-name-sub">Holdings Ltd</span>
</section>

</body>
</html>
```